Letterhead needed using basic elements of our new logo!

We have just had a new logo and business card created on Pixel Harbor and now would like a new letterhead for our company re-branding. Our logo inspires trust, professionalism and confidence and we would like to mirror that in our letterhead. We would like to use elements in our logo (as well as the logo itself, obviously), but understand with only a header and the ability to print in black and white, we are somewhat limited. We have also won the Resident's Pick Medal for best Property Management Company in our city and would like to somehow include that small banner (see uploaded file) in the letterhead, without it clashing?

Text to include:
Bright Cove Property Management (and logo)
C-214 Tamblyn Cres, Winnipeg, MB R2K 3P7
Ph: 204-739-8152
Fax: 1-888-376-2914
Email: customerservice@brightcovepropertymanagement.example
Web: www.brightcovepropertymanagement.example

Pasted below is our mission, vision and branding statements to help with the project:

Mission Statement

Provide the highest quality customer service to both property owners and tenants using innovative technology and well trained, caring staff.

Vision Statement

To redefine the way in which management is delivered to its customers, becoming the recognized leader in the property management industry.

Brand Essence

When our customers experience our product or service, it brings forth an emotion of absolute trust that we have their best interests at heart

Brand Personality

We are a company that is passionate about our customers, our company and our vision to be leaders in the field of property management. We are visionaries that aren't afraid to use cutting edge technologies to improve our products and service.

Position or Value Proposition

To whom are we speaking?
- real estate investors, including first timers that are giving us their first starter home. They are fairly naive, as they are not "big time" investors, and because they are giving us their first home (in contract to an investor buying a rental property, often sight unseen) they are more emotionally tied to their property and will require a company that inspires trust and confidence.

What is our brand promise?
- we will do our best to serve our clients, both owners and tenants, to give them prompt communication, clear, concise answers to their questions, and look after their property quickly and competently.

Why is our product different than the competition and why should our customers care?
- the current model used by most management companies employs individual portfolio managers that do things a little differently each instance, and differently than their fellow staff members. Our management product is superior because we use a combination of technology and strict procedures to ensure each client's experience is consistent, each and every time.

Industry/Entity Type

Business

Requirements
Must have
• We would like an option to be in black and white, to be able to be printed from Microsoft Word. As well, we do not want anything in a footer or any other kind of letterhead that bleeds below a header. The main use of this letterhead will be from our property management software, to be used in our form letters and other templates (sent to tenants and clients)
Should not have
• Footer or other elements where the text body would be, it will be used in a form letter

```html
<!DOCTYPE html>
<html lang="en">
<head>
<meta charset="utf-8">
<title>Bright Cove Property Management – Letterhead</title>
<link rel="stylesheet" href="https://fonts.googleapis.com/css2?family=Open+Sans:wght@400;600;700&display=swap">
<style>
  :root {
    --backdrop: #d9d9d9;
    --paper: #f4f4f4;
    --brand-blue: #4aa3d3;
    --brand-grey: #4a4d52;
    --text: #8a8a8a;
    --text-dark: #555;
  }
  * { box-sizing: border-box; margin: 0; padding: 0; }
  html, body {
    width: 1200px; height: 968px; overflow: hidden;
    background: var(--backdrop);
    font-family: "Open Sans", Arial, sans-serif;
  }
  .letterhead {
    position: absolute; left: 280px; top: 30px;
    width: 640px; height: 906px;
    background: var(--paper);
    box-shadow: 0 6px 24px rgba(0,0,0,.18);
    overflow: hidden;
  }
  .header-band {
    position: absolute; top: 0; right: 0;
    width: 340px; height: 24px;
    background: var(--brand-blue);
  }
  .brand {
    position: absolute; left: 56px; top: 78px;
    display: flex; align-items: center; gap: 8px;
  }
  .brand-mark {
    width: 18px; height: 18px; background: var(--brand-grey);
  }
  .brand-name {
    font-size: 15px; font-weight: 600; color: var(--brand-grey);
    letter-spacing: .3px;
  }
  .contact {
    position: absolute; right: 40px; top: 72px;
    text-align: right; font-size: 8px; line-height: 12px;
    color: var(--text-dark);
  }
  .letter-body {
    position: absolute; left: 56px; top: 150px; width: 528px;
    color: var(--text); font-size: 10.5px; line-height: 15px;
  }
  .salutation {
    font-size: 13px; font-weight: 600; color: var(--text);
    margin-bottom: 16px;
  }
  .letter-body p { margin-bottom: 14px; text-align: justify; }
  .sign-off {
    position: absolute; left: 56px; top: 560px; color: var(--text-dark);
  }
  .sign-name { font-size: 22px; color: #777; margin-bottom: 8px; }
  .sign-role { font-size: 8px; font-weight: 700; line-height: 11px; }
  .letter-date {
    position: absolute; right: 56px; bottom: 70px;
    font-size: 9px; font-weight: 700; color: var(--text-dark);
  }
</style>
</head>
<body>
  <main class="letterhead">
    <div class="header-band"></div>

    <div class="brand">
      <span class="brand-mark"></span>
      <span class="brand-name">Bright Cove Property Management</span>
    </div>

    <address class="contact">
      C-214 Tamblyn Cres, Winnipeg, MB R2K 3P7<br>
      Phone: 204-739-8152 &nbsp; Fax: 1-888-376-2914<br>
      customerservice@brightcovepropertymanagement.example<br>
      www.brightcovepropertymanagement.example
    </address>

    <section class="letter-body">
      <p class="salutation">Lorem ipsum dolor sit amet,</p>
      <p>Sed ut perspiciatis unde omnis iste natus error sit voluptatem accusantium doloremque laudantium, totam rem aperiam, eaque ipsa quae ab illo inventore veritatis et quasi architecto beatae vitae dicta sunt explicabo. Nemo enim ipsam voluptatem quia voluptas sit aspernatur aut odit aut fugit, sed quia consequuntur magni dolores eos qui ratione voluptatem sequi nesciunt. Neque porro quisquam est, qui dolorem ipsum quia dolor sit amet, consectetur, adipisci velit, sed quia non numquam eius modi tempora incidunt ut labore et dolore magnam aliquam quaerat voluptatem. Ut enim ad minima veniam, quis nostrum exercitationem ullam corporis suscipit laboriosam, nisi ut aliquid ex ea commodi consequatur? Quis autem vel eum iure reprehenderit qui in ea voluptate velit esse quam nihil molestiae consequatur, vel illum qui dolorem eum fugiat quo voluptas nulla pariatur.</p>
      <p>Sed ut perspiciatis unde omnis iste natus error sit voluptatem accusantium doloremque laudantium, totam rem aperiam, eaque ipsa quae ab illo inventore veritatis et quasi architecto beatae vitae dicta sunt explicabo. Nemo enim ipsam voluptatem quia voluptas sit aspernatur aut odit aut fugit, sed quia consequuntur magni dolores eos qui ratione voluptatem sequi nesciunt. Neque porro quisquam est, qui dolorem ipsum quia dolor sit amet, consectetur, adipisci velit, sed quia non numquam eius modi tempora incidunt ut labore et dolore magnam aliquam quaerat voluptatem. Ut enim ad minima veniam, quis nostrum exercitationem ullam corporis suscipit laboriosam, nisi ut aliquid ex ea commodi consequatur? Quis autem vel eum iure reprehenderit qui in ea voluptate velit esse quam nihil molestiae consequatur, vel illum qui dolorem eum fugiat quo voluptas nulla pariatur. Sed ut perspiciatis unde omnis iste natus error sit voluptatem accusantium doloremque laudantium, totam rem aperiam, eaque ipsa quae ab illo inventore veritatis et quasi architecto beatae vitae dicta sunt explicabo. Nemo enim ipsam voluptatem quia voluptas sit aspernatur aut odit aut fugit, sed quia consequuntur magni dolores eos qui ratione voluptatem sequi nesciunt. Neque porro quisquam est, qui dolorem ipsum quia dolor sit amet, consectetur, adipisci velit, sed quia non numquam eius modi tempora incidunt ut labore et dolore magnam aliquam quaerat voluptatem.</p>
    </section>

    <div class="sign-off">
      <p class="sign-name">John Doe</p>
      <p class="sign-role">Sincerely,<br>Managing Director</p>
    </div>

    <p class="letter-date">Date: 01 Jan, 2016</p>
  </main>
</body>
</html>
```